Netball Tour Opportunity Banner Ad

We need a banner ad designed in 2 specs (640px (w) x 150px (h) and 560px (w) x 478px (h)) both in 300dpi. Promoting a Junior Netball Tour opportunity to the United Kingdom. Attached logo and content from attached document should be incorporated into the design.
Ad should be designed to stand out and attract participants to the tour.

Target Market(s)

12-16 Year old female netballers and their parents

Industry/Entity Type

Travel

Requirements
Must have
• Must include Herons Logo

```html
<!DOCTYPE html>
<html lang="en">
<head>
<meta charset="utf-8">
<title>Herons Netball 2019 – UK Junior Development Tour Banners</title>
<link rel="stylesheet" href="https://fonts.googleapis.com/css2?family=Raleway:wght@600;700;800&family=Quicksand:wght@400;500&display=swap">
<style>
  :root{
    --canvas-bg:#e6e6e9;
    --panel-pink:#d17ed8;
    --curve-purple:#7b2a98;
    --grad-magenta:#c548d6;
    --grad-violet:#9a4fe0;
    --grad-blue:#6a62d6;
    --navy:#1f1640;
    --white:#ffffff;
    --yellow:#ffe93a;
    --ink:#15101f;
  }
  *{margin:0;padding:0;box-sizing:border-box}
  html,body{width:1200px;height:1200px;overflow:hidden}
  body{background:var(--canvas-bg);position:relative;font-family:"Raleway",sans-serif;font-variant-numeric:lining-nums}

  .banner{position:absolute;background:var(--panel-pink);overflow:hidden}
  .banner--square{left:222px;top:116px;width:752px;height:642px}
  .banner--strip{left:172px;top:876px;width:858px;height:199px}
  .banner__art{position:absolute;inset:0;width:100%;height:100%}

  .brand{position:absolute;display:flex;flex-direction:column;align-items:center;color:var(--navy);font-family:"Raleway",sans-serif;font-weight:800;text-align:center;line-height:1.05}
  .brand__dot{border-radius:50%;background:var(--navy);flex:none}
  .banner--square .brand{left:30px;top:90px;width:290px;font-size:54px;gap:14px}
  .banner--square .brand__dot{width:34px;height:34px}
  .banner--strip .brand{left:10px;top:44px;width:170px;font-size:28px;gap:8px}
  .banner--strip .brand__dot{width:18px;height:18px}

  .text{position:absolute;white-space:nowrap}
  .title{color:var(--white);font-weight:700;text-align:center;line-height:1.1}
  .subtitle{color:var(--white);font-weight:700;text-align:center;line-height:1.15}
  .open{color:var(--navy);font-weight:800;letter-spacing:-.2px}
  .teams{color:var(--yellow);font-weight:800}
  .features{list-style:none;color:var(--white);font-family:"Quicksand",sans-serif;font-weight:500}
  .info{font-family:"Quicksand",sans-serif;color:var(--white);font-weight:400}
  .info .contact{color:var(--ink);font-weight:500}

  /* square banner */
  .banner--square .title{left:390px;width:340px;top:100px;font-size:46px}
  .banner--square .subtitle{left:400px;width:320px;top:228px;font-size:31px}
  .banner--square .open{left:360px;width:392px;text-align:center;top:325px;font-size:20px}
  .banner--square .teams-line{left:360px;width:392px;text-align:center;top:350px;font-size:20px}
  .banner--square .features{left:420px;top:400px;font-size:23px;line-height:32.5px}
  .banner--square .info{left:24px;top:406px;font-size:23px;line-height:30px}
  .banner--square .contact-block{left:24px;top:532px;font-size:19px;line-height:32px}
  .banner--square .contact-block .plain{color:var(--white);font-size:22px}

  /* strip banner */
  .banner--strip .title{left:250px;width:524px;top:10px;font-size:29px}
  .banner--strip .subtitle{left:250px;width:524px;top:41px;font-size:25px}
  .banner--strip .open{left:296px;top:74px;font-size:13px}
  .banner--strip .features{left:299px;top:94px;font-size:14px;line-height:20px}
  .banner--strip .info{left:510px;top:106px;font-size:16px;line-height:21.5px}
</style>
</head>
<body>

<section class="banner banner--square" aria-label="Herons Netball 2019 tour banner, 560 by 478">
  <svg class="banner__art" viewBox="0 0 752 642" preserveAspectRatio="none" aria-hidden="true">
    <defs>
      <linearGradient id="tourGradSquare" x1="1" y1="0" x2="0" y2="1">
        <stop offset="0" style="stop-color:var(--grad-magenta)"/>
        <stop offset=".5" style="stop-color:var(--grad-violet)"/>
        <stop offset="1" style="stop-color:var(--grad-blue)"/>
      </linearGradient>
    </defs>
    <path d="M398 0 Q314 321 398 642 L752 642 L752 0 Z" fill="url(#tourGradSquare)"/>
    <path d="M392 -4 Q306 321 392 646" fill="none" style="stroke:var(--curve-purple)" stroke-width="11"/>
  </svg>

  <div class="brand"><span class="brand__dot"></span><span>Herons<br>Netball</span></div>

  <h1 class="text title">Herons Netball<br>2019</h1>
  <h2 class="text subtitle">UK Junior<br>Development Tour</h2>
  <p class="text open">OPEN TO INDIVIDUAL PLAYERS.</p>
  <p class="text teams teams-line">U13, U14, U15 &amp; U16 TEAMS</p>
  <ul class="text features">
    <li>- Elite Coaching</li>
    <li>- Netball Tournament</li>
    <li>- 2019 Netball World Cup</li>
    <li>- Stonehenge</li>
    <li>- Buckingham Palace</li>
  </ul>

  <p class="text info">For more information<br>or to register your<br>interest visit -</p>
  <p class="text info contact-block">
    <span class="contact">https://tourlink.net/heronsnetball</span><br>
    <span class="plain">or email</span><br>
    <span class="contact">enquiry@skyline.travel</span>
  </p>
</section>

<section class="banner banner--strip" aria-label="Herons Netball 2019 tour banner, 640 by 150">
  <svg class="banner__art" viewBox="0 0 858 199" preserveAspectRatio="none" aria-hidden="true">
    <defs>
      <linearGradient id="tourGradStrip" x1="1" y1="0" x2="0" y2="1">
        <stop offset="0" style="stop-color:var(--grad-magenta)"/>
        <stop offset=".55" style="stop-color:var(--grad-violet)"/>
        <stop offset="1" style="stop-color:var(--grad-blue)"/>
      </linearGradient>
    </defs>
    <path d="M214 0 Q186 100 214 199 L858 199 L858 0 Z" fill="url(#tourGradStrip)"/>
    <path d="M209 -3 Q181 100 209 202" fill="none" style="stroke:var(--curve-purple)" stroke-width="7"/>
  </svg>

  <div class="brand"><span class="brand__dot"></span><span>Herons<br>Netball</span></div>

  <h1 class="text title">Herons Netball 2019</h1>
  <h2 class="text subtitle">UK Junior Development Tour</h2>
  <p class="text open">OPEN TO INDIVIDUAL PLAYERS. <span class="teams">U13, U14, U15 &amp; U16 TEAMS</span></p>
  <ul class="text features">
    <li>- Elite Coaching</li>
    <li>- Netball Tournament</li>
    <li>- 2019 Netball World Cup</li>
    <li>- Stonehenge</li>
    <li>- Buckingham Palace</li>
  </ul>
  <p class="text info">For more information<br>or to register your interest<br>visit - <span class="contact">https://tourlink.net/heronsnetball</span><br>or email <span class="contact">enquiry@skyline.travel</span></p>
</section>

</body>
</html>
```